Cocktail-Making Assistant App re-design

Ok boys and girls, here's the deal:
I have an android app which is almost complete, but needs a design overhaul.

The app is a standard cocktail-making assistant: gives you a list of cocktails and the ability to see which cocktail you can make out of those ingredients (drinks, fruit, etc) you have at home.

I've attached some general app flow, as well as detailed requirements/explanation presentation. Most of those things are just FYI, so that you know what it's about.

3 screens are the most important (main screen, cocktail view screen, ingredient view screen), meaning I will pick the design mostly based on ideas for those 3 things, with the fourth being a rather simple list (given on attached flow, third tier)
Some other screens are derived from that, with some minor changes on it, but you shouldn't care about that.

There are lots of other, non-explained things which I said nothing about only because they are (from design point of view) completely the same and would only make it seem more complicated.

I don't want to influence the colour scheme, but the app will be released under RedFern developer name (having a light colured red fern as a logo) so I suppose some brownish design, for example, will not really fit nicely. If you, however, have a killer which you are confident will prove me wrong, I'm looking forward to seeing it!

It should be a serious, elegant look (as opposed to cartoonish, but we are not aiming for a business look at all!), not cluttered with details, no clubbing themes, glitter and so on.

Test apk file available on request (Android 2.3+).

Edit: payment is now guaranteed
Also please note that currently, the favorite, "heart" button has a motion effect:
on click it flies out of the screen to the left (white heart) and comes back to the screen as a red heart. Take that into consideration, if it means anything to you.
Updates

Target Market(s)

Whoever you imagine would enjoy drinking cocktails

Industry/Entity Type

Business

Requirements
Must have
• Everything is said in the provided documentation - images say more than I could possibly write here.
Nice to have
• As said, most of the icons are a nice-to-have. Only those which are critically linked to the rest of the design must be provided. More details in the docs.
Should not have
• No cartoon look, No zillion colours

```html
<!DOCTYPE html>
<html lang="en">
<head>
<meta charset="utf-8">
<title>Cocktail Search</title>
<link rel="stylesheet" href="https://fonts.googleapis.com/css2?family=Didact+Gothic&display=swap">
<style>
:root{
  --stage:#e8e9ea;
  --screen:#f3f3f3;
  --screen-glow:#ffffff;
  --bar-top:#6cbbdc;
  --bar-bottom:#a9d4e4;
  --ink:#1f1f1f;
  --muted:#6b6b6b;
  --icon:#7a7a7a;
  --field-line:#9a9a9a;
  --dot:#d3d3d4;
  --dot-active:#6a6b6e;
  --liquor:#e0cfa7;
  --mixer:#9fe7cd;
  --fruit:#d5f5d4;
  --garnish:#e2b8a7;
  --spirit:#cfe3f2;
  --all:#d6cbcf;
}
*{box-sizing:border-box;margin:0;padding:0}
html,body{width:1200px;height:1041px;overflow:hidden;background:var(--stage)}
body{position:relative;font-family:"Didact Gothic",sans-serif}
.screen{position:absolute;top:38px;width:549px;height:974px;
  background:radial-gradient(ellipse 70% 45% at 50% 30%,var(--screen-glow),var(--screen) 90%);overflow:hidden}
.screen--categories-b{left:48px}
.screen--categories-a{left:624px}
.app-bar{position:absolute;left:0;top:0;width:100%;height:91px;
  background:linear-gradient(var(--bar-top),var(--bar-bottom))}
.app-bar__title{position:absolute;left:0;right:0;top:23px;text-align:center;color:#fff;font-size:35px;letter-spacing:.3px}
.app-bar__btn{position:absolute;top:19px;width:56px;height:56px}
.app-bar__btn--home{left:17px}
.app-bar__btn--settings{left:476px}
.search-label{position:absolute;left:39px;top:118px;font-size:30px;color:var(--ink)}
.search-field{position:absolute;left:63px;top:173px;width:437px;height:50px;border:3px solid var(--field-line);background:#fff}
.search-field__hint{position:absolute;left:16px;top:10px;font-size:19px;color:#777}
.search-field__icon{position:absolute;right:10px;top:8px;width:30px;height:30px}
.category{position:absolute;height:159px;display:flex;align-items:center}
.category__icon{position:absolute}
.category__label{position:absolute;font-size:30px;color:var(--muted);white-space:nowrap}
.peek{position:absolute;left:0;width:30px;height:159px}
.pager{position:absolute;top:882px;display:flex;gap:28px}
.pager__dot{width:30px;height:30px;border-radius:50%;background:var(--dot)}
.pager__dot--active{background:var(--dot-active)}
svg.line{fill:none;stroke:var(--icon);stroke-width:3.5;stroke-linecap:round;stroke-linejoin:round}
</style>
</head>
<body>

<section class="screen screen--categories-b">
  <header class="app-bar">
    <svg class="app-bar__btn app-bar__btn--home" viewBox="0 0 56 56"><circle cx="28" cy="28" r="25" fill="none" stroke="#fff" stroke-width="3.5"/><path d="M15 29 L28 17 L41 29 H37 V39 H31 V32 H25 V39 H19 V29 Z" fill="#fff"/></svg>
    <h1 class="app-bar__title">Cocktail Search</h1>
  </header>
  <p class="search-label">Search</p>
  <div class="search-field"><span class="search-field__hint">Tap here to edit text&nbsp; . . .</span>
    <svg class="search-field__icon" viewBox="0 0 30 30"><circle cx="12" cy="12" r="8" fill="none" stroke="#d8d8d8" stroke-width="3.5"/><path d="M18 18 L27 27" stroke="#d8d8d8" stroke-width="5" stroke-linecap="round"/></svg></div>

  <div class="peek" style="top:319px;background:var(--liquor)"></div>
  <div class="category" style="left:30px;top:319px;width:497px;background:var(--mixer)">
    <svg class="category__icon line" style="left:40px;top:28px" width="64" height="96" viewBox="0 0 64 96"><rect x="10" y="4" width="44" height="14" rx="4"/><path d="M10 18 C2 22 2 30 2 38 V82 C2 88 6 92 12 92 H52 C58 92 62 88 62 82 V38 C62 30 62 22 54 18"/><path d="M14 56 H50 V74 H14 Z"/></svg>
    <span class="category__label" style="left:196px">Syrup / Mixer</span>
  </div>

  <div class="peek" style="top:487px;background:var(--fruit)"></div>
  <div class="category" style="left:30px;top:487px;width:497px;background:var(--garnish)">
    <svg class="category__icon line" style="left:20px;top:22px" width="160" height="110" viewBox="0 0 160 110"><path d="M20 96 L58 30"/><path d="M30 78 C14 70 8 56 14 42 C26 48 32 62 30 78Z"/><path d="M40 60 C34 42 40 28 54 20 C58 34 54 50 40 60Z"/><path d="M46 54 C60 46 74 50 82 62 C68 68 56 64 46 54Z"/><path d="M34 74 C46 70 60 74 66 84 C54 90 42 86 34 74Z"/><path d="M94 88 A30 30 0 0 1 150 66 Z"/><path d="M102 84 A22 22 0 0 1 142 68"/><path d="M122 78 L118 64 M122 78 L132 66 M122 78 L108 72"/></svg>
    <span class="category__label" style="left:196px">Garnish / Spice</span>
  </div>

  <div class="peek" style="top:655px;background:var(--spirit)"></div>
  <div class="category" style="left:30px;top:655px;width:497px;background:var(--all)">
    <svg class="category__icon line" style="left:20px;top:42px" width="170" height="80" viewBox="0 0 170 80"><path d="M8 24 H50 L44 74 H14 Z"/><path d="M12 44 H46"/><path d="M30 24 L20 6 H8"/><path d="M66 6 H102 C104 30 96 44 84 44 C72 44 64 30 66 6Z"/><path d="M84 44 V72 M72 74 H96"/><path d="M122 12 H162 V24 H122 Z"/><path d="M126 24 L130 74 H154 L158 24"/><path d="M128 6 H156"/></svg>
    <span class="category__label" style="left:231px">All</span>
  </div>

  <nav class="pager" style="left:197px"><span class="pager__dot"></span><span class="pager__dot pager__dot--active"></span><span class="pager__dot"></span></nav>
</section>

<section class="screen screen--categories-a">
  <header class="app-bar">
    <svg class="app-bar__btn app-bar__btn--home" viewBox="0 0 56 56"><circle cx="28" cy="28" r="25" fill="none" stroke="#fff" stroke-width="3.5"/><path d="M15 29 L28 17 L41 29 H37 V39 H31 V32 H25 V39 H19 V29 Z" fill="#fff"/></svg>
    <h1 class="app-bar__title">Cocktail Search</h1>
    <svg class="app-bar__btn app-bar__btn--settings" viewBox="0 0 56 56"><circle cx="28" cy="28" r="25" fill="none" stroke="#fff" stroke-width="3.5"/><g fill="#fff"><circle cx="28" cy="28" r="11"/><rect x="25" y="12" width="6" height="32" rx="1"/><rect x="25" y="12" width="6" height="32" rx="1" transform="rotate(45 28 28)"/><rect x="25" y="12" width="6" height="32" rx="1" transform="rotate(90 28 28)"/><rect x="25" y="12" width="6" height="32" rx="1" transform="rotate(135 28 28)"/></g><circle cx="28" cy="28" r="4.5" fill="var(--bar-top)"/></svg>
  </header>
  <p class="search-label">Search</p>
  <div class="search-field"><span class="search-field__hint">Tap here to edit text&nbsp; . . .</span>
    <svg class="search-field__icon" viewBox="0 0 30 30"><circle cx="12" cy="12" r="8" fill="none" stroke="#d8d8d8" stroke-width="3.5"/><path d="M18 18 L27 27" stroke="#d8d8d8" stroke-width="5" stroke-linecap="round"/></svg></div>

  <div class="category" style="left:26px;top:319px;width:501px;background:var(--liquor)">
    <svg class="category__icon line" style="left:36px;top:24px" width="70" height="106" viewBox="0 0 70 106"><path d="M12 4 H20 V24 C28 32 30 40 30 48 V98 C30 101 28 102 26 102 H6 C4 102 2 101 2 98 V48 C2 40 4 32 12 24 Z"/><path d="M50 4 H58 V24 C66 32 68 40 68 48 V98 C68 101 66 102 64 102 H44 C42 102 40 101 40 98 V48 C40 40 42 32 50 24 Z"/></svg>
    <span class="category__label" style="left:161px">Liquor / Cordial</span>
  </div>

  <div class="category" style="left:26px;top:487px;width:501px;background:var(--fruit)">
    <svg class="category__icon line" style="left:48px;top:20px" width="60" height="118" viewBox="0 0 60 118"><path d="M6 28 H48 C50 44 46 58 40 64 C36 68 34 72 34 78 C34 84 36 88 38 90 H16 C18 88 20 84 20 78 C20 72 18 68 14 64 C8 58 4 44 6 28Z"/><path d="M10 50 C20 54 34 46 46 50"/><path d="M27 90 V110 M12 112 H42"/><path d="M24 28 L50 4 H58"/><path d="M18 22 L12 12 L6 22Z"/></svg>
    <span class="category__label" style="left:161px">Fruit / Juice</span>
  </div>

  <div class="category" style="left:26px;top:655px;width:501px;background:var(--spirit)">
    <svg class="category__icon line" style="left:32px;top:22px" width="80" height="116" viewBox="0 0 80 116"><path d="M4 30 H58 L31 64 Z"/><path d="M31 64 V108 M16 110 H46"/><path d="M26 50 L62 8 L72 4"/><path d="M12 40 C22 44 36 40 50 40"/></svg>
    <span class="category__label" style="left:161px">Other Spirit</span>
  </div>

  <nav class="pager" style="left:190px"><span class="pager__dot pager__dot--active"></span><span class="pager__dot"></span><span class="pager__dot"></span></nav>
</section>

</body>
</html>
```